Book Cover: Unmasking The Crooked Ledger with KELM-Gate

I'm looking for a book cover for my pending book. I do NOT want any AI-generated image with its notoriously-slick AI imagery.
The Title is: "Unmasking The Crooked Ledger with KELM-Gate" with the lengthy added subtitle "The Pathway to Permanently Restore Our American Republic, Outside the Election Process, Almost Overnight."
Also on the front cover--author name of "Dale Hutchins" (lower on the cover).
Parameters or things to consider:
1. Please separate the title from the subtitle with a colon, and emphasize the title greatly over the long subtitle.
2. "The Crooked Ledger" is ultimately a "bad" thing (because it cleverly hides federal action beyond the spirit of the Constitution).
3. Since abolishing a "bad" thing is a good thing, "Abolishing" should reflect that positive note, and perhaps be larger font, perhaps slanted (symbolically cancelling then "The Crooked Ledger").
4. "KELM-Gate" is a "good" thing, too, as it's the method to end the bad thing.
5. On the subtitle, much smaller fonts to keep all that text from overwhelming the front cover.
6. Please allow 3/8" for bleed and then still keep all text well away (3/8" or more) from those trim edges.
7. The book will be 6" X 9", and probably 1" thick (~400 pages). Overall dimensions will be 13.75" WX 9 .75" H (again, 3/8" bleed X 4).
8. For the back cover, but I'll just put a white box over most of the back, and then add the text later (before print submission). Continue colors of front onto back (but no real graphic needed).
9. For the cover graphic, I was thinking that an old country road may work well, because of the relevance of the fictional metaphor that is found in Chapter 3 of this non-fiction book. However, I'm not sure if this image will prove successful (even as the story provides a great visual for the premise of the book).
10. Spine: Title and author last name only is fine (no subtitle or first name of author).
Basically, I'm thinking of a long-ago rural road, perhaps in Utah (fictionally), with generic red rock formations in the background, and largely desert views surrounding the roadway. The simple road itself needn't necessarily be paved, but no more than one lane in each direction and not a lot of modern street markings.
I prefer the approach road to the T-Intersection be more-visible -- at a closer-perspective -- as it travels from the lower left of the front cover, slightly upwards, at a growing distance, towards the right side of the book, but ending well before the book's right edge, at a formal "T-Intersection," with this crossroad at 90 degrees perpendicular to the approach road.
This crossroad then will come from the (lower) right of the book, heading somewhat slantwise to the (upper) left area of the book generally, with the approach road largely hitting the crossroad largely centered at the T-Intersection, or slightly to the right of center.
There should be some sort of simple American-styled stop sign (not necessarily modern design) in the normal position, found before the crossroad, at the right lane. No vehicles.
AFTER the crossroad, at the far side of the T-Intersection, the storyline describes a solid hard-rock wall, maybe 10' or 15' high, parallel with the crossroad, but not so insurmountable that the rock wall couldn't later be excavated/demolished and partially removed, so that the approach road would later continue forward, initially at street level, but much later even with an overpass (so plan the terrain beyond the T-Intersection accordingly, that an overpass from the approach road could continue forward from the stop sign, that currently only offers a left or right path).
In-between the far side of the crossroad and the rock wall, there should be some sort of crude arrow sign, serving as a simple notice or barrier against travelling forward, notifying people to turn either right or left.
That arrow sign pointing right could also say "Enumerated Powers" and the sign pointing left can point to "Inherent Powers".
Again, the signs should be simple (more appropriate for long-ago, rather than modern).
In the story, decades later, the rock wall gets excavated first for a ground-level road, that in time became a multi-lane formal overpass and freeway, that largely ends up hiding the old T-Intersection from open view, but importantly, NEVER REMOVES OR FULLY OBSCURES the T-Intersection, or right-path road (the overpass gets shifted a little left from the approach road [with the approach road then becoming the one-way off-ramp, down to the stop sign, from the new freeway forward]).
It may be unworkable, but perhaps the primary shaded-in view would be that initial/earliest scene described above, but perhaps a stick or outline future-vision-view (like an engineering draft, for example) could overlay or outline an overpass and formal freeway continuing forward.
Again, though, the original T-Intersection can't be fully obscured or torn down with the new freeway design, even as it could be partially obscured.
I am open though, to other ideas on the cover, but I just don't know what they would be.
The design ultimately should reflect 200 years of incremental federal treachery, imposed primarily by our courts (with improper action resting upon invalid and dishonest activity [yet when properly-challenged, may be overcome {think of Pip in The Lantern of Brindle, pulling back the curtain to expose the self-proclaiming wizard of unlimited power, who was only a fraud}]).
Please note that although The Marvelous Lantern of Brindle book is now in the public domain, the 1939 movie is still copyrighted (so no visuals based on the movie), in any alternate designs.
Conservative Americans interested in restoring individual liberty and limited government under the U.S. Constitution and our country's founding principles

```html
<!DOCTYPE html>
<html lang="en">
<head>
<meta charset="utf-8">
<title>Unmasking The Crooked Ledger with KELM-Gate — Cover Wrap</title>
<link rel="stylesheet" href="https://fonts.googleapis.com/css2?family=Abril+Fatface&family=Playfair+Display:wght@700;900&family=Oswald:wght@500;600;700&family=Open+Sans:wght@700&display=swap">
<style>
  :root {
    --sky-deep: #1b3560;
    --sky-mid: #3f6796;
    --sky-light: #9fb6cf;
    --sunset: #f0a040;
    --sunset-glow: #f7d27a;
    --desert: #a9774a;
    --desert-dark: #6e4a2c;
    --road: #c9a27a;
    --spine: #151f2b;
    --gold-light: #f6dcaa;
    --gold-dark: #b8853f;
    --title-red: #8e1c17;
    --accent-red: #b3241c;
    --white: #ffffff;
    --cream: #efe0c2;
    --parchment: #e9e3d2;
  }
  * { margin: 0; padding: 0; box-sizing: border-box; }
  html, body { width: 1200px; height: 851px; overflow: hidden; background: #222; }

  .cover-wrap { position: relative; width: 1200px; height: 851px; overflow: hidden; }

  .scene {
    position: absolute; inset: 0;
    background:
      radial-gradient(ellipse 260px 140px at 1150px 400px, rgba(247,210,122,.95), rgba(240,160,64,.55) 45%, rgba(240,160,64,0) 100%),
      linear-gradient(180deg, var(--sky-deep) 0%, var(--sky-mid) 22%, var(--sky-light) 40%, #c9a983 50%, var(--desert) 58%, #b58a5c 70%, var(--road) 82%, var(--desert-dark) 100%);
  }

  /* Back cover */
  .back-quote-block { position: absolute; left: 60px; width: 454px; top: 36px; text-align: center; }
  .star-rule { display: block; width: 454px; height: 20px; }
  .back-quote {
    font-family: "Playfair Display", serif; font-weight: 900; color: var(--white);
    font-size: 23px; line-height: 36px; letter-spacing: .3px; text-transform: uppercase;
    margin: 8px 0 10px;
  }
  .back-copy-frame { position: absolute; left: 36px; top: 179px; width: 498px; height: 638px; }

  /* Spine */
  .spine { position: absolute; left: 556px; top: 0; width: 86px; height: 851px; background: var(--spine); }
  .spine-text {
    position: absolute; left: 43px; top: 30px;
    transform-origin: 0 0; transform: rotate(90deg) translateY(-50%);
    white-space: nowrap; display: flex; align-items: center; height: 60px;
  }
  .spine-lead { font-family: "Abril Fatface", serif; color: var(--accent-red); font-size: 40px; letter-spacing: 1px; margin-right: 16px; transform: skewX(-10deg); display: inline-block; }
  .spine-title { font-family: "Oswald", sans-serif; font-weight: 600; color: var(--white); font-size: 34px; letter-spacing: 2px; }
  .spine-author {
    position: absolute; left: 43px; top: 678px; transform-origin: 0 0; transform: rotate(90deg) translateY(-50%);
    font-family: "Oswald", sans-serif; font-weight: 500; color: var(--accent-red); font-size: 19px; letter-spacing: 1px; white-space: nowrap;
  }

  /* Front cover */
  .front { position: absolute; left: 642px; top: 0; width: 558px; height: 851px; text-align: center; }
  .lead-word-wrap { position: absolute; left: 24px; top: 26px; width: 490px; height: 150px; transform: rotate(-7deg); }
  .lead-swash { position: absolute; left: -6px; top: 98px; width: 330px; height: 36px; }
  .lead-word {
    position: absolute; left: 0; right: 0; top: 0;
    font-family: "Abril Fatface", serif; font-size: 94px; line-height: 1;
    background: linear-gradient(180deg, var(--gold-light) 10%, #e9bb74 55%, var(--gold-dark) 100%);
    -webkit-background-clip: text; background-clip: text; color: transparent;
    filter: drop-shadow(3px 4px 0 rgba(40,20,10,.7));
  }
  .title-rule-row { position: absolute; left: 0; width: 558px; display: flex; align-items: center; justify-content: center; gap: 10px; }
  .title-the { top: 140px; }
  .title-with { top: 308px; }
  .rule-line { height: 2px; background: var(--cream); }
  .rule-star { width: 12px; height: 12px; fill: var(--gold-dark); }
  .small-word { font-family: "Playfair Display", serif; font-weight: 900; color: var(--white); font-size: 28px; text-shadow: 2px 2px 0 rgba(0,0,0,.6); }
  .main-title {
    position: absolute; left: 0; width: 558px; top: 172px;
    font-family: "Playfair Display", serif; font-weight: 900; color: var(--white);
    font-size: 72px; line-height: 66px; letter-spacing: 1px;
    text-shadow: 3px 3px 0 rgba(0,0,0,.75);
  }
  .method-name {
    position: absolute; left: 0; width: 558px; top: 344px;
    font-family: "Abril Fatface", serif; color: var(--title-red); font-size: 62px; line-height: 62px; letter-spacing: 1px;
    text-shadow: -1px -1px 0 var(--cream), 1px 1px 0 var(--cream), 3px 3px 0 rgba(0,0,0,.55);
  }
  .method-star { position: absolute; left: 273px; top: 406px; width: 12px; height: 12px; fill: var(--title-red); }
  .subtitle {
    position: absolute; left: 0; width: 558px; top: 420px;
    font-family: "Open Sans", sans-serif; font-weight: 700; color: var(--white); font-size: 12.5px; line-height: 21px;
    text-shadow: 1px 1px 2px rgba(0,0,0,.8);
  }
  .author {
    position: absolute; left: 0; width: 558px; top: 738px;
    font-family: "Oswald", sans-serif; font-weight: 600; color: var(--cream); font-size: 44px; line-height: 54px; letter-spacing: 1.5px;
    text-shadow: 2px 2px 2px rgba(0,0,0,.6);
  }
  .author-rule { position: absolute; left: 127px; top: 797px; width: 300px; height: 2px; background: var(--accent-red); }
</style>
</head>
<body>
<main class="cover-wrap">
  <div class="scene" role="img" aria-label="Desert landscape at sunset: red rock formations, an old dirt road approaching a T-intersection with a low rock wall, crude arrow signs reading Inherent Powers and Enumerated Powers, and an old stop sign"></div>

  <!-- Back cover -->
  <section class="back-cover">
    <div class="back-quote-block">
      <svg class="star-rule" viewBox="0 0 454 20" aria-hidden="true">
        <line x1="0" y1="10" x2="214" y2="10" stroke="#efe0c2" stroke-width="2"/>
        <line x1="240" y1="10" x2="454" y2="10" stroke="#efe0c2" stroke-width="2"/>
        <polygon points="227,1 230,8 238,8 232,13 234,20 227,16 220,20 222,13 216,8 224,8" fill="#d9a766"/>
      </svg>
      <p class="back-quote">“ Restore the Republic.<br>Reclaim our Liberty.”</p>
      <svg class="star-rule" viewBox="0 0 454 20" aria-hidden="true">
        <line x1="0" y1="10" x2="214" y2="10" stroke="#efe0c2" stroke-width="2"/>
        <line x1="240" y1="10" x2="454" y2="10" stroke="#efe0c2" stroke-width="2"/>
        <polygon points="227,1 230,8 238,8 232,13 234,20 227,16 220,20 222,13 216,8 224,8" fill="#d9a766"/>
      </svg>
    </div>
    <svg class="back-copy-frame" viewBox="0 0 498 638" aria-hidden="true">
      <path d="M14 2 H484 A12 12 0 0 0 496 14 V624 A12 12 0 0 0 484 636 H14 A12 12 0 0 0 2 624 V14 A12 12 0 0 0 14 2 Z" fill="none" stroke="#ffffff" stroke-width="2"/>
      <path d="M18 7 H480 A11 11 0 0 0 491 18 V620 A11 11 0 0 0 480 631 H18 A11 11 0 0 0 7 620 V18 A11 11 0 0 0 18 7 Z" fill="#e9e3d2" stroke="#ffffff" stroke-width="1.5"/>
    </svg>
  </section>

  <!-- Spine -->
  <section class="spine">
    <div class="spine-text"><span class="spine-lead">Unmasking</span><span class="spine-title">THE CROOKED LEDGER</span></div>
    <div class="spine-author">HUTCHINS</div>
  </section>

  <!-- Front cover -->
  <section class="front">
    <div class="lead-word-wrap">
      <svg class="lead-swash" viewBox="0 0 330 36" aria-hidden="true">
        <path d="M0 22 C90 12 210 5 330 0 L326 16 C220 22 110 30 4 36 Z" fill="#8e1c17"/>
      </svg>
      <div class="lead-word">Unmasking</div>
    </div>

    <div class="title-rule-row title-the">
      <span class="rule-line" style="width:130px"></span>
      <svg class="rule-star" viewBox="0 0 20 20"><polygon points="10,0 13,7 20,7 14,12 16,20 10,15 4,20 6,12 0,7 7,7"/></svg>
      <span class="small-word">THE</span>
      <svg class="rule-star" viewBox="0 0 20 20"><polygon points="10,0 13,7 20,7 14,12 16,20 10,15 4,20 6,12 0,7 7,7"/></svg>
      <span class="rule-line" style="width:130px"></span>
    </div>

    <h1 class="main-title">CROOKED<br>LEDGER</h1>

    <div class="title-rule-row title-with">
      <span class="rule-line" style="width:160px"></span>
      <span class="small-word">WITH</span>
      <span class="rule-line" style="width:160px"></span>
    </div>

    <div class="method-name">KELM - GATE</div>
    <svg class="method-star" viewBox="0 0 20 20" aria-hidden="true"><polygon points="10,0 13,7 20,7 14,12 16,20 10,15 4,20 6,12 0,7 7,7"/></svg>

    <p class="subtitle">The Roadmap to Lastingly Renew Our Constitutional Order,<br>Beyond the Ballot Box, Nearly at Once.</p>

    <div class="author">DALE HUTCHINS</div>
    <span class="author-rule"></span>
  </section>
</main>
</body>
</html>
```